Jasmine Gin Bottle Label

I need a label design for a gin bottle. We are a small, farm based distillery producing hand crafted spirits. I've attached a mock-up of a wrap label on the bottle we use. I'd like to see imagery of Jasmin flower(s) in the label.
Our logo is attached.

Target Market(s)

Adults of legal drinking age who enjoy quality spirits

Industry/Entity Type

Alcoholic beverage production

Requirements
Must have
• Logo displayed. Details on label as follows: 750 mL 40% alc/vol
Nice to have
• I like contrast is a design

```html
<!DOCTYPE html>
<html lang="en">
<head>
<meta charset="utf-8">
<title>Jasmine Gin Label</title>
<link rel="stylesheet" href="https://fonts.googleapis.com/css2?family=Rye&family=Yellowtail&family=Oswald:wght@500&display=swap">
<style>
  :root {
    --paper: #ffffff;
    --ink: #0c0c0c;
    --copper: #a8764a;
    --copper-soft: #e6d3bf;
    --stage: #efefef;
  }
  html, body {
    margin: 0;
    width: 1200px;
    height: 1200px;
    overflow: hidden;
    background: var(--stage);
  }
  .label {
    position: absolute;
    left: 105px;
    top: 50px;
    width: 990px;
    height: 1100px;
    display: block;
  }
  .label-paper { fill: var(--paper); }
  .frame-line { fill: none; stroke: var(--copper); stroke-width: 1.4; }
  .frame-dots { fill: none; stroke: var(--copper); stroke-width: 2; stroke-dasharray: 0.1 4.5; stroke-linecap: round; }
  .corner-ornament { fill: var(--copper-soft); }
  .star-panel { fill: var(--ink); }
  .brand-name {
    font-family: "Oswald", sans-serif;
    font-weight: 500;
    fill: var(--paper);
    letter-spacing: 2px;
  }
  .brand-dot { fill: none; stroke: var(--copper); stroke-width: 1.6; }
  .product-name {
    font-family: "Rye", serif;
    fill: var(--paper);
  }
  .product-type {
    font-family: "Yellowtail", cursive;
    fill: var(--copper);
  }
  .flower-cluster { fill: url(#bloomTone); }
  .spec-text {
    font-family: "Oswald", sans-serif;
    font-weight: 500;
    fill: var(--paper);
    letter-spacing: 1px;
  }
  .spec-rule { stroke: var(--paper); stroke-width: 1.3; }
  .spec-arrow { fill: var(--paper); }
</style>
</head>
<body>
<svg class="label" viewBox="0 0 562 624" xmlns="http://www.w3.org/2000/svg" aria-label="Jasmine Gin label">
  <defs>
    <radialGradient id="bloomTone" cx="50%" cy="50%" r="60%">
      <stop offset="0%" stop-color="#f2ece4"/>
      <stop offset="100%" stop-color="#8c6440"/>
    </radialGradient>
  </defs>

  <rect class="label-paper" x="0" y="0" width="562" height="624"/>

  <!-- frame -->
  <rect class="frame-line" x="4" y="4" width="554" height="616"/>
  <rect class="frame-dots" x="11" y="11" width="540" height="602"/>
  <rect class="frame-line" x="32" y="44" width="498" height="536"/>

  <!-- corner flourishes: slim L-shaped areas in the gaps beside the panel -->
  <g class="corner-ornaments">
    <path class="corner-ornament" role="img" aria-label="Copper flourish ornament, top left"
          d="M38 50 H150 V70 H60 V180 H38 Z"/>
    <path class="corner-ornament" role="img" aria-label="Copper flourish ornament, top right"
          d="M524 50 H412 V70 H502 V180 H524 Z"/>
    <path class="corner-ornament" role="img" aria-label="Copper flourish ornament, bottom left"
          d="M38 574 H150 V554 H60 V444 H38 Z"/>
    <path class="corner-ornament" role="img" aria-label="Copper flourish ornament, bottom right"
          d="M524 574 H412 V554 H502 V444 H524 Z"/>
  </g>

  <!-- central star panel -->
  <polygon class="frame-line" points="281,8 558,314 281,620 4,314"/>
  <g class="star-panel">
    <polygon points="281,26 537,314 281,602 25,314"/>
    <rect x="66" y="84" width="430" height="455"/>
  </g>

  <!-- brand -->
  <g class="brand">
    <circle class="brand-dot" cx="281" cy="124" r="9"/>
    <text class="brand-name" x="281" y="166" text-anchor="middle" font-size="22">STONEBROOK</text>
    <text class="brand-name" x="281" y="188" text-anchor="middle" font-size="12" letter-spacing="4">DISTILLERY</text>
  </g>

  <!-- flowers -->
  <g class="flowers">
    <ellipse class="flower-cluster" role="img" aria-label="Jasmine blossoms with copper leaves" cx="140" cy="210" rx="52" ry="32"/>
    <ellipse class="flower-cluster" role="img" aria-label="Jasmine blossoms with copper leaves" cx="422" cy="210" rx="52" ry="32"/>
    <ellipse class="flower-cluster" role="img" aria-label="Jasmine blossoms with copper leaves" cx="140" cy="408" rx="52" ry="30"/>
    <ellipse class="flower-cluster" role="img" aria-label="Jasmine blossoms with copper leaves" cx="422" cy="408" rx="52" ry="30"/>
    <ellipse class="flower-cluster" role="img" aria-label="Cluster of jasmine blossoms" cx="272" cy="512" rx="50" ry="40"/>
  </g>

  <!-- product name -->
  <text class="product-name" x="281" y="352" text-anchor="middle" font-size="84" textLength="420" lengthAdjust="spacingAndGlyphs">JASMINE</text>
  <text class="product-type" x="286" y="428" text-anchor="middle" font-size="70">Gin</text>

  <!-- specs -->
  <g class="spec spec-volume">
    <line class="spec-rule" x1="106" y1="474" x2="198" y2="474"/>
    <polygon class="spec-arrow" points="102,474 108,471 108,477"/>
    <text class="spec-text" x="142" y="500" text-anchor="middle" font-size="16">750 ML</text>
    <line class="spec-rule" x1="106" y1="514" x2="198" y2="514"/>
    <polygon class="spec-arrow" points="102,514 108,511 108,517"/>
  </g>
  <g class="spec spec-strength">
    <line class="spec-rule" x1="364" y1="474" x2="456" y2="474"/>
    <polygon class="spec-arrow" points="460,474 454,471 454,477"/>
    <text class="spec-text" x="418" y="500" text-anchor="middle" font-size="16">40% ABV</text>
    <line class="spec-rule" x1="364" y1="514" x2="456" y2="514"/>
    <polygon class="spec-arrow" points="460,514 454,511 454,517"/>
  </g>
</svg>
</body>
</html>
```